Maplecrest Apartments Downtown Northport

We are looking to redesign our entry way sign at Maplecrest Apartments, a low density residential apartment building, located in Downtown Northport, Alabama, U.S. Downtown Northport is a bustling boutique business district with a small town feel comprised of shops, restaurants, and a renowned arts community known for Varrow Arts Center and Festival which is one of the nation's top outdoor arts festivals. Maplecrest Apartments and its sign is the first thing you seen when you enter Downtown Northport. We are looking to redesign our sign, entry way and landscaping to compliment the building and character of the historic downtown.

Target Market(s)

Our apartment building is comprised of 20 apartments units with tenants who are primarily part of the local workforce, young professionals, or students at the Halverton College or other nearby institutions.

Requirements
Must have
• The name of the apartment building - Maplecrest
Phone number on the sign 205-555-0148

```html
<!DOCTYPE html>
<html lang="en">
<head>
<meta charset="utf-8">
<title>Maplecrest Entry Sign</title>
<link rel="stylesheet" href="https://fonts.googleapis.com/css2?family=Satisfy&family=Roboto+Condensed:wght@700&display=swap">
<style>
  :root {
    --page-bg: #ffffff;
    --panel-dark: #4b4a3d;
    --band-taupe: #8b8776;
    --brick-light: #ecebe8;
    --pill-dark: #2e2e2e;
    --pill-edge: #555555;
    --text-light: #ffffff;
    --shadow-dark: #2a291f;
  }
  html, body {
    margin: 0;
    padding: 0;
    width: 947px;
    height: 1200px;
    overflow: hidden;
    background: var(--page-bg);
  }
  .canvas {
    position: relative;
    width: 947px;
    height: 1200px;
  }
  .entry-sign {
    position: absolute;
    left: 33px;
    top: 418px;
    width: 880px;
    height: 365px;
    display: block;
  }
  .sign-name {
    font-family: "Satisfy", cursive;
    font-size: 138px;
    fill: var(--text-light);
    stroke: var(--band-taupe);
    stroke-width: 1.5px;
    paint-order: stroke;
    filter: drop-shadow(3px 4px 0 var(--shadow-dark));
  }
  .sign-phone {
    font-family: "Roboto Condensed", sans-serif;
    font-weight: 700;
    font-size: 60px;
    fill: var(--text-light);
  }
</style>
</head>
<body>
<div class="canvas">
  <svg class="entry-sign" viewBox="0 0 880 365" xmlns="http://www.w3.org/2000/svg">
    <defs>
      <linearGradient id="pillShade" x1="0" y1="0" x2="0" y2="1">
        <stop offset="0" stop-color="var(--pill-edge)"/>
        <stop offset="0.5" stop-color="var(--pill-dark)"/>
        <stop offset="1" stop-color="#1f1f1f"/>
      </linearGradient>
    </defs>

    <rect class="panel-backdrop" x="0" y="0" width="880" height="365" fill="var(--panel-dark)" role="img" aria-label="Dark painted brick wall texture"/>

    <path class="accent-band" d="M0,219 C200,245 300,298 440,298 C600,298 750,264 880,252 L880,365 L0,365 Z" fill="var(--band-taupe)"/>

    <path class="brick-base" d="M0,288 C200,298 300,330 440,330 C600,330 750,286 880,272 L880,365 L0,365 Z" fill="var(--brick-light)" role="img" aria-label="White brick wall texture"/>

    <text class="sign-name" x="440" y="180" text-anchor="middle">Maplecrest</text>

    <g class="phone-pill">
      <rect x="183" y="262" width="512" height="70" rx="35" fill="url(#pillShade)"/>
      <circle class="phone-icon-disc" cx="232" cy="297" r="24" fill="var(--text-light)"/>
      <path class="phone-icon" d="M223,285 c2,-2 4,-2 5,0 l3,5 c1,2 0,3 -1,4 l-2,1 c1,3 4,6 7,7 l1,-2 c1,-1 2,-2 4,-1 l5,3 c2,1 2,3 0,5 l-2,2 c-3,3 -10,0 -16,-6 c-6,-6 -8,-12 -6,-15 z" fill="var(--pill-dark)"/>
      <text class="sign-phone" x="266" y="319">205-555-0148</text>
    </g>
  </svg>
</div>
</body>
</html>
```